Google Form Graphic to suit our Brand and industry

Create a graphic / image for us to put at the top of our client enquiry google form.
The image will be a section of an architectural home with our branding over the top. Preferably translucent.
The image must suit the shape of the google forms image, which is an elongated rectangle
#003d5d - brand colour

Target Market(s)

residential home owners, high end architectural homes

Industry/Entity Type

Residential construction

Colors
0054AA
0677BA
7BADD7
CADEEF
E8F1F8

Requirements
Must have
• our branding and a photo of an architectural home in the background

```html
<!DOCTYPE html>
<html lang="en">
<head>
<meta charset="utf-8">
<title>Harbourline Homes – Form Header Banners</title>
<link rel="stylesheet" href="https://fonts.googleapis.com/css2?family=Montserrat:wght@600&display=swap">
<style>
  :root {
    --brand-navy: #003d5d;
    --backdrop: #c5bca7;
    --white: #ffffff;
    --veil: rgba(255, 255, 255, 0.55);
  }
  * { margin: 0; padding: 0; box-sizing: border-box; }
  html, body {
    width: 720px;
    height: 1200px;
    overflow: hidden;
    background: var(--backdrop);
  }
  .banner-set {
    position: absolute;
    left: 40px;
    top: 215px;
    width: 640px;
    display: flex;
    flex-direction: column;
    gap: 30px;
  }
  .form-banner {
    position: relative;
    width: 640px;
    height: 160px;
    border-radius: 10px;
    overflow: hidden;
    box-shadow: 0 6px 14px rgba(0, 0, 0, 0.12);
  }
  .form-banner svg {
    position: absolute;
    inset: 0;
    display: block;
  }
  .brand-name {
    position: absolute;
    left: 0;
    top: 0;
    width: 240px;
    height: 160px;
    display: flex;
    align-items: center;
    justify-content: center;
    font-family: "Montserrat", sans-serif;
    font-weight: 600;
    font-size: 20px;
    letter-spacing: 0.01em;
    color: var(--white);
    white-space: nowrap;
  }
</style>
</head>
<body>
<main class="banner-set">

  <section class="form-banner">
    <svg width="640" height="160" viewBox="0 0 640 160">
      <defs>
        <linearGradient id="tone-exterior" x1="0" y1="0" x2="1" y2="1">
          <stop offset="0" stop-color="#eef2f7"/>
          <stop offset="0.45" stop-color="#c9a878"/>
          <stop offset="0.8" stop-color="#5a5d61"/>
          <stop offset="1" stop-color="#3d4246"/>
        </linearGradient>
      </defs>
      <rect class="photo-area" role="img" aria-label="Photo of a modern timber-clad architectural home against a pale sky" x="230" y="0" width="410" height="160" fill="url(#tone-exterior)"/>
      <rect class="photo-veil" x="230" y="0" width="410" height="160" fill="var(--veil)"/>
      <path class="navy-panel" d="M0 0 H291 L243 70 Q237 80 243 90 L291 160 H0 Z" fill="var(--brand-navy)"/>
      <path class="chevron-line" d="M615 -5 L578 40 Q570 52 578 64 L645 132" fill="none" stroke="var(--white)" stroke-width="14" stroke-opacity="0.85"/>
    </svg>
    <p class="brand-name">Harbourline Homes</p>
  </section>

  <section class="form-banner">
    <svg width="640" height="160" viewBox="0 0 640 160">
      <defs>
        <linearGradient id="tone-facade" x1="0" y1="0" x2="0" y2="1">
          <stop offset="0" stop-color="#b9d2ea"/>
          <stop offset="0.4" stop-color="#f1f3f4"/>
          <stop offset="0.8" stop-color="#d6d9dc"/>
          <stop offset="1" stop-color="#7b8590"/>
        </linearGradient>
      </defs>
      <rect class="photo-area" role="img" aria-label="Photo of a white two-storey weatherboard home with a grey garage door under blue sky" x="230" y="0" width="410" height="160" fill="url(#tone-facade)"/>
      <rect class="photo-veil" x="230" y="0" width="410" height="160" fill="rgba(255,255,255,0.35)"/>
      <path class="navy-panel" d="M0 0 H291 L243 70 Q237 80 243 90 L291 160 H0 Z" fill="var(--brand-navy)"/>
      <path class="chevron-line" d="M615 -5 L578 40 Q570 52 578 64 L645 132" fill="none" stroke="var(--white)" stroke-width="14" stroke-opacity="0.9"/>
    </svg>
    <p class="brand-name">Harbourline Homes</p>
  </section>

  <section class="form-banner">
    <svg width="640" height="160" viewBox="0 0 640 160">
      <defs>
        <linearGradient id="tone-kitchen" x1="0" y1="0" x2="0" y2="1">
          <stop offset="0" stop-color="#f4f5f6"/>
          <stop offset="0.55" stop-color="#e6e8e8"/>
          <stop offset="1" stop-color="#c69a6c"/>
        </linearGradient>
      </defs>
      <rect class="photo-area" role="img" aria-label="Photo of a bright white kitchen with an island bench, pendant lights and timber floor" x="230" y="0" width="410" height="160" fill="url(#tone-kitchen)"/>
      <rect class="photo-veil" x="230" y="0" width="410" height="160" fill="var(--veil)"/>
      <path class="navy-panel" d="M0 0 H291 L243 70 Q237 80 243 90 L291 160 H0 Z" fill="var(--brand-navy)"/>
      <path class="chevron-line" d="M615 -5 L578 40 Q570 52 578 64 L645 132" fill="none" stroke="var(--white)" stroke-width="14" stroke-opacity="0.9"/>
    </svg>
    <p class="brand-name">Harbourline Homes</p>
  </section>

  <section class="form-banner">
    <svg width="640" height="160" viewBox="0 0 640 160">
      <defs>
        <linearGradient id="tone-patio" x1="0" y1="0" x2="1" y2="1">
          <stop offset="0" stop-color="#f2f3f3"/>
          <stop offset="0.5" stop-color="#b7bfb3"/>
          <stop offset="1" stop-color="#6f7670"/>
        </linearGradient>
      </defs>
      <rect class="photo-area" role="img" aria-label="Photo of a covered outdoor living patio with dining set, lounge and garden" x="230" y="0" width="410" height="160" fill="url(#tone-patio)"/>
      <rect class="photo-veil" x="230" y="0" width="410" height="160" fill="var(--veil)"/>
      <path class="navy-panel" d="M0 0 H291 L243 70 Q237 80 243 90 L291 160 H0 Z" fill="var(--brand-navy)"/>
      <path class="chevron-line" d="M615 -5 L578 40 Q570 52 578 64 L645 132" fill="none" stroke="var(--white)" stroke-width="14" stroke-opacity="0.9"/>
    </svg>
    <p class="brand-name">Harbourline Homes</p>
  </section>

</main>
</body>
</html>
```